Tending Our Garden eBook Cover Design

I want to deisgn a cover for my eBook (FRONT COVER) and the title is:

What I Grew From a Single Spark. And Why It Matters
By KT Dorran

TITLE CHANGED TO: UNDER THE WILLOW TREE; WHERE I FOUND MY QUIET STRENGTH AND WHERE YOU MIGHT TOO

The color palette is attached. Along with some photos options of me. Along with the ebook in WORD Document. My website is www.KTDorranLive.example. You can use a different color palette if you think it is best

Target Market(s)

women who look to build a personal brand

Industry/Entity Type

health and wellness

Requirements
Must have
• the title
Nice to have
• use my picture on the cover; but that is optional
Should not have
• any men

```html
<!DOCTYPE html>
<html lang="en">
<head>
<meta charset="utf-8">
<title>Under the Willow Tree — eBook Cover</title>
<link rel="stylesheet" href="https://fonts.googleapis.com/css2?family=League+Gothic&family=Kalam:wght@400&display=swap">
<style>
  :root {
    --stage: #eeeeee;
    --paper: #fbfbfa;
    --paper-shade: #f1f1ef;
    --ink: #111111;
    --leaf: #3a8c46;
    --leaf-soft: rgba(58, 140, 70, 0.85);
    --blossom-soft: rgba(226, 65, 107, 0.8);
    --hair: #2a1d18;
    --skin: #b98467;
    --top: #e8431d;
    --sign: #ffffff;
  }
  * { box-sizing: border-box; margin: 0; padding: 0; }
  html, body {
    width: 1200px; height: 857px; overflow: hidden;
    background: var(--stage);
  }
  .stage { position: relative; width: 1200px; height: 857px; }
  .cover {
    position: absolute; left: 300px; top: 18px;
    width: 600px; height: 820px; overflow: hidden;
    background: radial-gradient(ellipse at 50% 30%, var(--paper) 40%, var(--paper-shade) 100%);
  }
  .wings {
    position: absolute; left: 0; top: 290px; width: 600px; height: 530px;
    background:
      radial-gradient(ellipse 210px 330px at 90px 300px, var(--leaf-soft) 0%, rgba(58,140,70,0.35) 55%, rgba(58,140,70,0) 100%),
      radial-gradient(ellipse 200px 330px at 520px 290px, var(--blossom-soft) 0%, rgba(226,65,107,0.35) 55%, rgba(226,65,107,0) 100%);
  }
  .portrait {
    position: absolute; left: 200px; top: 405px; width: 225px; height: 415px;
    border-radius: 110px 110px 0 0;
    background: linear-gradient(180deg, var(--hair) 0%, var(--hair) 14%, var(--skin) 30%, var(--skin) 62%, var(--top) 72%, var(--top) 100%);
  }
  .title {
    position: absolute; left: 0; width: 600px; display: block;
    font-family: "League Gothic", "Oswald", sans-serif;
    font-weight: 400;
    text-align: center; line-height: 0.8; text-transform: uppercase;
    white-space: nowrap;
  }
  .title-lead { top: 40px; font-size: 116px; color: var(--ink); }
  .title-key { top: 138px; font-size: 127px; color: var(--ink); }
  .title-key .accent { color: var(--leaf); }
  .tagline { font-size: 34px; letter-spacing: 5px; color: var(--ink); }
  .tagline-one { top: 270px; }
  .tagline-two { top: 314px; }
  .author {
    position: absolute; left: 218px; top: 752px; width: 190px;
    font-family: "Kalam", cursive; font-size: 34px; color: var(--sign);
    text-align: center; transform: rotate(-4deg);
  }
</style>
</head>
<body>
  <main class="stage">
    <section class="cover">
      <div class="wings" role="img" aria-label="Soft feathered wings, green on the left and pink on the right"></div>
      <div class="portrait" role="img" aria-label="Portrait photo of the author smiling in a red top"></div>
      <h1>
        <span class="title title-lead">Under the</span>
        <span class="title title-key"><span class="accent">Willow</span> Tree;</span>
        <span class="title tagline tagline-one">Where I found my quiet strength</span>
        <span class="title tagline tagline-two">and where you might too</span>
      </h1>
      <p class="author">KT Dorran</p>
    </section>
  </main>
</body>
</html>
```